Concise,Good colour matching,Good looks design for "HERD SURE QUICK ASSAY FOR LIVESTOCK"

Product Positioning: Affordable test for Large Animals (Livestock/Veterinary Use)
Product Name: HERD SURE Quick Assay Kit (for large animals, e.g., cattle, horses, swine,Avian,sheep).

2. Packaging Requirements

A. Visual Design
Color Scheme:
Green/Blue/Orange/Yellow/Red/Gray/White(chose 2~4 colors)

Mandatory Info:
Brand logo ("HERD SURE")

Target Market(s)

Southeast Asia, Africa, Middle East, South America

Industry/Entity Type

Veterinary diagnostic for LIVESTOCK

Colors

Designer to choose colors to be used in the design.

Requirements
Nice to have
• Concise,Good colour matching,Good looks

```html
<!DOCTYPE html>
<html lang="en">
<head>
<meta charset="utf-8">
<title>HERD SURE Quick Assay Kit – Packaging Panels</title>
<link href="https://fonts.googleapis.com/css2?family=Anton&family=Oswald:wght@600&family=Arimo:wght@400;700&display=swap" rel="stylesheet">
<style>
  :root {
    --sky: #36a9e1;
    --navy: #0e3f6b;
    --band-start: #0d9de0;
    --band-mid: #5a5f8c;
    --band-end: #e30613;
    --white: #ffffff;
    --ink: #222222;
    --art-light: rgba(124,196,234,0.75);
    --art-dark: rgba(28,95,150,0.85);
    --art-clear: rgba(54,169,225,0);
    --frame: #dfe7ee;
    --page: #ffffff;
  }
  * { margin: 0; padding: 0; box-sizing: border-box; }
  html, body { width: 716px; height: 1200px; overflow: hidden; background: var(--page); }
  .canvas { position: relative; width: 716px; height: 1200px; }

  /* Side info panel */
  .info-panel {
    position: absolute; left: 38px; top: 22px; width: 640px; height: 306px;
    background: var(--white); border: 1px solid var(--frame);
    padding: 22px 44px;
    font-family: "Arimo", sans-serif; color: var(--ink);
  }
  .info-title {
    font-family: "Anton", sans-serif; font-weight: 400; color: var(--sky);
    font-size: 34px; line-height: 1.1; letter-spacing: 0.5px; margin-bottom: 14px;
  }
  .feature { margin-bottom: 10px; }
  .feature:last-child { margin-bottom: 0; }
  .feature-head { color: var(--sky); font-size: 19px; line-height: 1.2; }
  .feature-body { font-size: 14px; line-height: 1.35; }
  .feature-body b { font-weight: 700; }

  /* Front label panels */
  .label {
    position: absolute; left: 38px; width: 640px;
    background: var(--sky); overflow: hidden;
  }
  .label--large { top: 350px; height: 440px; }
  .label--small { top: 830px; height: 330px; }

  .label-art {
    position: absolute;
    background: radial-gradient(closest-side, var(--art-dark) 0%, var(--art-light) 55%, var(--art-clear) 100%);
  }
  .label--large .label-art { left: 300px; top: 0; width: 340px; height: 330px; }
  .label--small .label-art { left: 390px; top: 0; width: 250px; height: 222px; }

  .brand {
    position: absolute; font-family: "Anton", sans-serif; font-weight: 400; color: var(--navy);
    line-height: 1; white-space: nowrap;
  }
  .label--large .brand { left: 92px; top: 248px; font-size: 68px; }
  .label--small .brand { left: 92px; top: 148px; font-size: 64px; }

  .band {
    position: absolute; left: 0; width: 100%;
    background: linear-gradient(90deg, var(--band-start) 0%, var(--band-mid) 50%, var(--band-end) 100%);
  }
  .label--large .band { top: 332px; height: 28px; }
  .label--small .band { top: 222px; height: 27px; }

  .tagline {
    position: absolute; left: 0; width: 100%; text-align: center;
    font-family: "Oswald", sans-serif; font-weight: 600; color: var(--white);
    font-size: 27px; line-height: 1.3; letter-spacing: 0.3px;
  }
  .label--large .tagline { top: 366px; }
  .label--small .tagline { top: 255px; }
</style>
</head>
<body>
<div class="canvas">

  <section class="info-panel">
    <h2 class="info-title">HERD SURE RAPID TEST</h2>
    <div class="feature">
      <div class="feature-head">Fast &amp; Efficient:</div>
      <p class="feature-body">Rapid test <b>results in less than 10 minutes</b><br>from prep to completion.</p>
    </div>
    <div class="feature">
      <div class="feature-head">Affordable:</div>
      <p class="feature-body">"Colloidal gold-based rapid tests that combine<br>high accuracy with cost-effectiveness."</p>
    </div>
    <div class="feature">
      <div class="feature-head">Reliable &amp; Simple:</div>
      <p class="feature-body">Stable test performance with 2~30°C,<br>Easy to operate, no professional skills required.</p>
    </div>
  </section>

  <section class="label label--large">
    <div class="label-art" role="img" aria-label="Blue pencil-sketch illustration of a pig, a horse, a duck and chickens"></div>
    <h1 class="brand">HERD SURE</h1>
    <div class="band"></div>
    <p class="tagline">Affordable Diagnostics for Healthy Herds</p>
  </section>

  <section class="label label--small">
    <div class="label-art" role="img" aria-label="Blue pencil-sketch illustration of a pig, a horse, a duck and chickens"></div>
    <h1 class="brand">HERD SURE</h1>
    <div class="band"></div>
    <p class="tagline">Affordable Diagnostics for Healthy Herds</p>
  </section>

</div>
</body>
</html>
```